Tilwa Sandrim Construction
Business Cards, Note Pads, Envelopes, Letterhead , signboard etc.
Bright & Fun-filled
Hamdan R. Al-Qutami
CEO
P.O Box 40573
Al-Hassa 36417
Saudi Arabia
Hamdan@tilwasandrim.com.sa
www.tilwasandrim.com.sa
Leave the back of the business card to write all the information in arabic
similar logo

```html
<!DOCTYPE html>
<html lang="en">
<head>
<meta charset="utf-8">
<title>Tilwa Sandrim Construction – Stationery</title>
<link href="https://fonts.googleapis.com/css2?family=Montserrat:wght@700;800&family=Open+Sans:wght@400;600;700&display=swap" rel="stylesheet">
<style>
:root{
  --red:#c4161c;
  --red-dark:#9e1015;
  --bg-top:#f2d2cc;
  --bg-bottom:#c51b1f;
  --paper:#ffffff;
  --paper-shade:#f1f1f1;
  --ink:#555555;
  --ink-light:#9a9a9a;
  --line:#d6d6d6;
}
*{box-sizing:border-box;margin:0;padding:0}
html,body{width:1200px;height:638px;overflow:hidden}
body{
  position:relative;
  background:linear-gradient(180deg,var(--bg-top) 0%,#e58a80 45%,var(--bg-bottom) 100%);
  font-family:"Open Sans",Arial,sans-serif;
  color:var(--ink);
}
.sheet{position:absolute;background:var(--paper);box-shadow:0 3px 10px rgba(80,0,0,.35)}
.brand{
  font-family:"Montserrat",Arial,sans-serif;font-weight:800;color:var(--red);
  letter-spacing:.5px;line-height:1;display:flex;align-items:center;gap:5px;
}
.brand .mark{width:9px;height:9px;background:var(--red)}
.brand.on-red{color:#fff}
.brand.on-red .mark{background:#fff}

/* business card front */
.card{width:187px;height:112px;left:36px;overflow:hidden}
.card--one{top:209px}
.card--two{top:340px}
.card__band{position:absolute;left:0;top:0;width:100%;height:40px;background:var(--red)}
.card__name{position:absolute;right:10px;top:9px;text-align:left;width:96px;color:#fff;font-weight:700;font-size:8.5px;line-height:1.2}
.card__title{font-weight:400;font-size:6px}
.card .brand{position:absolute;left:10px;top:50px;font-size:11px}
.card__tag{position:absolute;left:10px;top:63px;font-size:4.5px;color:var(--ink-light);letter-spacing:.3px}
.card__info{position:absolute;left:92px;top:46px;font-size:4.6px;line-height:1.45;color:var(--ink)}
.card__info b{color:var(--red);font-weight:700}

/* business card back */
.card-back{width:190px;height:112px;left:242px}
.card-back--one{top:209px}
.card-back--two{top:340px}
.card-back__pattern{position:absolute;inset:0;background:linear-gradient(135deg,#ffffff 0%,var(--paper-shade) 100%)}
.card-back .brand{position:absolute;right:10px;bottom:10px;font-size:8px}

/* envelopes */
.envelope{overflow:hidden}
.envelope--rear{left:168px;top:446px;width:288px;height:106px}
.envelope--middle{left:100px;top:475px;width:236px;height:113px}
.envelope__flap{position:absolute;left:0;top:0;width:100%;height:60%}
.envelope--front{left:240px;top:516px;width:240px;height:122px}
.envelope__band{position:absolute;left:0;top:0;width:100%;height:16px;background:var(--red)}
.envelope--front .brand{position:absolute;left:12px;top:26px;font-size:11px}
.envelope__address{position:absolute;left:12px;top:48px;font-size:5px;line-height:1.5;color:var(--ink)}

/* letterheads */
.letter{top:182px;width:314px;height:456px;overflow:hidden}
.letter--plain{left:509px}
.letter--form{left:833px}
.letter__head{position:absolute;left:0;top:0;width:100%;height:40px;background:var(--red)}
.letter__head .brand{position:absolute;left:12px;top:15px;font-size:12px}
.letter__contact{position:absolute;right:10px;top:7px;text-align:right;color:#fff;font-size:4.3px;line-height:1.55}
.letter__rule{position:absolute;left:0;top:42px;width:100%;height:2px;background:var(--line)}
.letter__emblem{position:absolute;left:107px;top:262px;width:100px;height:100px;border-radius:50%;background:var(--red);opacity:.08}
.letter__foot{position:absolute;left:0;bottom:0;width:100%;height:6px;background:var(--red)}

/* form */
.form{position:absolute;left:14px;top:60px;width:286px;font-size:5px;color:var(--ink)}
.form__cols{display:flex;gap:18px}
.form__col{flex:1}
.form__row{display:flex;align-items:flex-end;gap:4px;height:11px}
.form__row span{width:26px}
.form__row i{flex:1;border-bottom:.6px solid var(--line);height:7px}
.form__checks{display:flex;gap:14px;margin-top:12px}
.form__checks label{display:flex;align-items:center;gap:3px}
.form__checks label::before{content:"";width:5px;height:5px;border:.6px solid var(--ink-light)}
.form__comments{margin-top:10px}
</style>
</head>
<body>

<!-- business cards, front -->
<div class="sheet card card--one">
  <div class="card__band"></div>
  <div class="card__name">Hamdan R. Al-Qutami<br><span class="card__title">CEO</span></div>
  <div class="brand"><span class="mark"></span>TILWA</div>
  <div class="card__tag">SANDRIM CONSTRUCTION</div>
  <div class="card__info">
    P.O Box 40573<br>Al-Hassa 36417<br>Saudi Arabia<br>
    <b>Phone :</b> +966 13 580 2214<br>
    <b>Fax :</b> +966 13 580 2215<br>
    <b>Mobile :</b> +966 55 410 7380<br>
    <b>Email :</b> Hamdan@tilwasandrim.com.sa<br>
    <b>Web :</b> www.tilwasandrim.com.sa
  </div>
</div>
<div class="sheet card card--two">
  <div class="card__band"></div>
  <div class="card__name">Hamdan R. Al-Qutami<br><span class="card__title">CEO</span></div>
  <div class="brand"><span class="mark"></span>TILWA</div>
  <div class="card__tag">SANDRIM CONSTRUCTION</div>
  <div class="card__info">
    P.O Box 40573<br>Al-Hassa 36417<br>Saudi Arabia<br>
    <b>Phone :</b> +966 13 580 2214<br>
    <b>Fax :</b> +966 13 580 2215<br>
    <b>Mobile :</b> +966 55 410 7380<br>
    <b>Email :</b> Hamdan@tilwasandrim.com.sa<br>
    <b>Web :</b> www.tilwasandrim.com.sa
  </div>
</div>

<!-- business cards, back -->
<div class="sheet card-back card-back--one">
  <div class="card-back__pattern" role="img" aria-label="Faint repeating house-roof pattern in light grey"></div>
  <div class="brand"><span class="mark"></span>TILWA SANDRIM</div>
</div>
<div class="sheet card-back card-back--two">
  <div class="card-back__pattern" role="img" aria-label="Faint repeating house-roof pattern in light grey"></div>
  <div class="brand"><span class="mark"></span>TILWA SANDRIM</div>
</div>

<!-- envelopes -->
<div class="sheet envelope envelope--rear">
  <svg class="envelope__flap" viewBox="0 0 288 64" preserveAspectRatio="none"><polygon points="0,0 288,0 144,64" fill="var(--red)"/></svg>
</div>
<div class="sheet envelope envelope--middle">
  <svg class="envelope__flap" viewBox="0 0 236 68" preserveAspectRatio="none"><polygon points="0,0 236,0 118,68" fill="var(--red)"/></svg>
</div>
<div class="sheet envelope envelope--front">
  <div class="envelope__band"></div>
  <div class="brand"><span class="mark"></span>TILWA SANDRIM</div>
  <div class="envelope__address">P.O Box 40573<br>Al-Hassa 36417<br>Saudi Arabia</div>
</div>

<!-- letterhead -->
<div class="sheet letter letter--plain">
  <div class="letter__head">
    <div class="brand on-red"><span class="mark"></span>TILWA SANDRIM</div>
    <div class="letter__contact">
      P.O Box 40573, Al-Hassa 36417, Saudi Arabia<br>
      Phone: +966 13 580 2214 &nbsp; Fax: +966 13 580 2215<br>
      Email: Hamdan@tilwasandrim.com.sa &nbsp; Web: www.tilwasandrim.com.sa
    </div>
  </div>
  <div class="letter__rule"></div>
  <div class="letter__emblem"></div>
  <div class="letter__foot"></div>
</div>

<!-- note pad / enquiry form -->
<div class="sheet letter letter--form">
  <div class="letter__head">
    <div class="brand on-red"><span class="mark"></span>TILWA SANDRIM</div>
    <div class="letter__contact">
      P.O Box 40573, Al-Hassa 36417, Saudi Arabia<br>
      Phone: +966 13 580 2214 &nbsp; Fax: +966 13 580 2215<br>
      Email: Hamdan@tilwasandrim.com.sa &nbsp; Web: www.tilwasandrim.com.sa
    </div>
  </div>
  <div class="letter__rule"></div>
  <div class="form">
    <div class="form__cols">
      <div class="form__col">
        <div class="form__row"><span>Name</span><i></i></div>
        <div class="form__row"><span>Phone</span><i></i></div>
        <div class="form__row"><span>Project</span><i></i></div>
        <div class="form__row"><span>Plans</span><i></i></div>
      </div>
      <div class="form__col">
        <div class="form__row"><span>Email</span><i></i></div>
        <div class="form__row"><span>Date</span><i></i></div>
        <div class="form__row"><span>Location</span><i></i></div>
        <div class="form__row"><span>Budget</span><i></i></div>
      </div>
    </div>
    <div class="form__checks">
      <label>Villa</label><label>Commercial</label><label>Interior Design</label><label>Renovation</label><label>Other</label>
    </div>
    <div class="form__comments">Comments:</div>
  </div>
  <div class="letter__emblem"></div>
  <div class="letter__foot"></div>
</div>

</body>
</html>
```